Business Card Design for videographer/filmmaker - Dale Voss

Looking for a professional, creative, eye catching business card.
Target Market(s)
high end, big budget, businesses, producers, filmmakers, and studios
Industry/Entity Type
Business
Contact Information for Business Card
Please be creative and submit something original.
Font styles to use
Requirements
Must have
- Dale Voss
- creative producer, writer, director, cinematographer, editor
- Pre-production, production, post-production

```html
<!DOCTYPE html>
<html lang="en">
<head>
<meta charset="utf-8">
<title>Voss Films – Dale Voss Business Card</title>
<link href="https://fonts.googleapis.com/css2?family=Advent+Pro:wght@300;400;700&display=swap" rel="stylesheet">
<style>
  :root {
    --backdrop: #e6e0d6;
    --card: #0c1517;
    --ink: #ffffff;
    --ink-soft: #e4e6e6;
    --ink-muted: #aeb4b5;
    --decor: #474d4e;
  }
  * { margin: 0; padding: 0; box-sizing: border-box; }
  html, body {
    width: 1200px;
    height: 961px;
    overflow: hidden;
    background: var(--backdrop);
  }
  .stage {
    position: relative;
    width: 1200px;
    height: 961px;
    font-family: "Advent Pro", sans-serif;
  }
  .card {
    position: absolute;
    left: 265px;
    width: 643px;
    height: 358px;
    background: var(--card);
    overflow: hidden;
  }
  .card--front { top: 81px; }
  .card--back { top: 515px; }

  .wordmark {
    position: absolute;
    color: var(--ink);
    font-family: "Advent Pro", sans-serif;
    font-weight: 700;
    line-height: 1;
  }
  .wordmark__name { display: block; }
  .wordmark__tag { display: block; }

  .card--front .wordmark { left: 52px; top: 144px; }
  .card--front .wordmark__name { font-size: 86px; letter-spacing: 14px; }
  .card--front .wordmark__tag { font-size: 34px; margin: 8px 0 0 12px; letter-spacing: 22px; }

  .front-decor {
    position: absolute;
    left: 400px;
    top: 0;
    width: 243px;
    height: 358px;
  }

  .card--back .brand-dot {
    position: absolute;
    left: 40px;
    top: 40px;
    width: 110px;
    height: 110px;
    border-radius: 50%;
    background: var(--ink);
  }
  .card--back .wordmark { left: 191px; top: 88px; }
  .card--back .wordmark__name { font-size: 60px; letter-spacing: 10px; }
  .card--back .wordmark__tag { font-size: 26px; margin: 4px 0 0 8px; letter-spacing: 16px; }

  .person { position: absolute; left: 22px; top: 238px; color: var(--ink); width: 380px; }
  .person__name { font-weight: 300; font-size: 36px; line-height: 1; }
  .person__role { font-weight: 700; font-size: 14px; line-height: 17px; margin-top: 8px; }
  .person__phases {
    font-weight: 400;
    font-size: 13px;
    line-height: 16px;
    margin-top: 7px;
    color: var(--ink-muted);
    letter-spacing: 0.5px;
  }

  .contact {
    position: absolute;
    left: 413px;
    top: 248px;
    color: var(--ink-soft);
    font-weight: 300;
    font-size: 18px;
    line-height: 26.5px;
    list-style: none;
  }
  .contact__label { display: inline-block; width: 34px; }
</style>
</head>
<body>
<main class="stage">
  <section class="card card--front">
    <div class="wordmark">
      <span class="wordmark__name">VOSS</span>
      <span class="wordmark__tag">films</span>
    </div>
    <svg class="front-decor" viewBox="0 0 243 358" role="img" aria-label="Faint brand emblem decoration">
      <circle cx="130" cy="190" r="105" fill="var(--decor)" opacity="0.55"/>
    </svg>
  </section>

  <section class="card card--back">
    <span class="brand-dot"></span>
    <div class="wordmark">
      <span class="wordmark__name">VOSS</span>
      <span class="wordmark__tag">films</span>
    </div>
    <div class="person">
      <p class="person__name">Dale Voss</p>
      <p class="person__role">Creative Producer, Writer, Director,<br>Cinematographer, Editor</p>
      <p class="person__phases">Pre-production · Production · Post-production</p>
    </div>
    <ul class="contact">
      <li><span class="contact__label">T</span>123456789</li>
      <li><span class="contact__label">M</span>123456789</li>
      <li><span class="contact__label">E</span>hello@vossfilms.com</li>
      <li><span class="contact__label">W</span>www.vossfilms.com</li>
    </ul>
  </section>
</main>
</body>
</html>
```